Defense Attorney Business Card Design Project/ Stationary

I am looking for a distinctive business card design for my solo law practice.
I practice criminal defense, both juvenile and adult, including DUI. I am a very experienced attorney with prior military experience. The design should convey a traditional, old school flair, but not be too stodgy or uptight. Some color. My logo should appear.

Project Deadline Extended Reason: I misunderstood how this project works and I was not prepared with my logo when this project ran the first time. Added Thursday, November 13, 2014

Reason: I was sent overseas on military duty last year, which interrupted this project. Thank you for your participation... I hope we can get this done this week! Thank you, Des

Target Market(s)

Regular everyday people looking for strong, knowledgeable, authoritative representation while they are faced with criminal charges. Many have never been charged with a crime before. A reassuring air is therefore desired.

Industry/Entity Type

Business

Contact Information for Business Card

My information is:
Desmond R. Whitcombe, Attorney at Law
735 Linden Avenue Suite 300
Oakland, California 94618
Tel: (510) 555-0183
Fax: (510) 555-0162
email: deswhitcombelaw@mailbrook.net
web: www.deswhitcombelaw.net

Font styles to use
Serif
Sans Serif
Decorative

Colors
0255a3
ffffff

Requirements
Must have
• Sharp lines, bold elements. Conservative use of colors, such as deep blues, burgundy, grays for example.
• While my logo says "Des Whitcombe", it should be modified to show "Desmond R. Whitcombe".
Should not have
• Cliche imagery such as scales of justice, gavels, Tower of Varenholt, etc.

```html
<!DOCTYPE html>
<html lang="en">
<head>
<meta charset="utf-8">
<title>Des Whitcombe Law — Stationery</title>
<link rel="stylesheet" href="https://fonts.googleapis.com/css2?family=Cinzel:wght@400;600&family=Lato:wght@400;700&display=swap">
<style>
  :root {
    --navy: #073a55;
    --paper: #ffffff;
    --ink: #1f2a33;
    --muted: #5b6770;
    --backdrop: #8f9486;
    --serif: "Cinzel", "Times New Roman", serif;
    --sans: "Lato", Arial, sans-serif;
  }
  * { box-sizing: border-box; margin: 0; padding: 0; }
  html, body { width: 1200px; height: 1000px; overflow: hidden; }
  body { background: var(--backdrop); font-family: var(--sans); color: var(--ink); position: relative; }

  .piece { position: absolute; box-shadow: 0 6px 16px rgba(0,0,0,.25); overflow: hidden; }

  /* Wordmark */
  .wordmark { display: flex; flex-direction: column; align-items: center; }
  .wordmark__name { font-family: var(--serif); font-weight: 600; letter-spacing: .04em; white-space: nowrap; display: flex; align-items: center; gap: .45em; }
  .wordmark__mark { width: .55em; height: .55em; background: currentColor; display: inline-block; }
  .wordmark__rule { height: 1px; background: currentColor; align-self: stretch; margin: .35em 0 .3em; }
  .wordmark__tag { font-family: var(--serif); letter-spacing: .25em; white-space: nowrap; }
  .wordmark--navy { color: var(--navy); }
  .wordmark--white { color: var(--paper); }

  .contact { font-size: 7.5px; line-height: 1.55; color: var(--ink); }
  .contact dt { display: inline; font-weight: 700; }
  .contact dd { display: inline; }
  .contact div { white-space: nowrap; }

  /* Letterhead */
  .letterhead { left: 20px; top: 217px; width: 400px; height: 566px; background: var(--paper); }
  .letterhead .wordmark { position: absolute; left: 34px; top: 40px; font-size: 17px; }
  .letterhead .wordmark__tag { font-size: 8px; }
  .letterhead .contact { position: absolute; right: 34px; top: 112px; }
  .letterhead__footer-tag { position: absolute; right: 34px; bottom: 22px; font-family: var(--serif); font-size: 8px; letter-spacing: .25em; color: var(--navy); }
  .letterhead__band { position: absolute; left: 0; right: 0; bottom: 0; height: 8px; background: var(--navy); }

  /* Presentation folder */
  .folder { left: 450px; top: 217px; width: 400px; height: 566px; background: var(--navy); }
  .folder .wordmark { position: absolute; left: 0; right: 60px; top: 90px; font-size: 22px; }
  .folder .wordmark__tag { font-size: 10px; }
  .folder__pocket-line { position: absolute; top: 0; bottom: 0; right: 48px; width: 2px; background: var(--paper); }

  /* Envelope */
  .envelope { left: 880px; top: 217px; width: 300px; height: 150px; background: var(--paper); }
  .envelope .wordmark { position: absolute; left: 20px; top: 18px; font-size: 11px; }
  .envelope .wordmark__tag { font-size: 5.5px; }
  .envelope .contact { position: absolute; right: 20px; bottom: 16px; font-size: 6px; }

  /* Business card front */
  .card-front { left: 880px; top: 404px; width: 300px; height: 171px; background: var(--navy); display: flex; align-items: center; justify-content: center; }
  .card-front .wordmark { font-size: 18px; }
  .card-front .wordmark__tag { font-size: 8px; }

  /* Business card back */
  .card-back { left: 880px; top: 612px; width: 300px; height: 171px; background: var(--paper); }
  .card-back .wordmark { position: absolute; left: 18px; top: 16px; font-size: 10px; }
  .card-back .wordmark__tag { font-size: 5px; }
  .card-back__name { position: absolute; left: 18px; top: 64px; font-size: 9px; font-weight: 700; color: var(--navy); }
  .card-back .contact { position: absolute; left: 18px; top: 84px; font-size: 7px; }
  .card-back__address { position: absolute; right: 18px; top: 108px; font-size: 7px; line-height: 1.55; text-align: right; color: var(--ink); font-style: normal; }
  .card-back__band { position: absolute; left: 0; right: 0; bottom: 0; height: 10px; background: var(--navy); }
</style>
</head>
<body>

  <section class="piece letterhead" aria-label="Letterhead">
    <div class="wordmark wordmark--navy">
      <span class="wordmark__name"><span class="wordmark__mark"></span>Des Whitcombe Law</span>
      <span class="wordmark__rule"></span>
      <span class="wordmark__tag">Attorney at Law</span>
    </div>
    <dl class="contact">
      <div><dt>Tel:</dt> <dd>(510) 555-0183</dd></div>
      <div><dt>Fax:</dt> <dd>(510) 555-0162</dd></div>
      <div><dt>Email:</dt> <dd>deswhitcombelaw@mailbrook.net</dd></div>
      <div><dt>Web:</dt> <dd>www.deswhitcombelaw.net</dd></div>
    </dl>
    <p class="letterhead__footer-tag">Attorney at Law</p>
    <div class="letterhead__band"></div>
  </section>

  <section class="piece folder" aria-label="Presentation folder">
    <div class="wordmark wordmark--white">
      <span class="wordmark__name"><span class="wordmark__mark"></span>Des Whitcombe Law</span>
      <span class="wordmark__rule"></span>
      <span class="wordmark__tag">Attorney at Law</span>
    </div>
    <div class="folder__pocket-line"></div>
  </section>

  <section class="piece envelope" aria-label="Envelope">
    <div class="wordmark wordmark--navy">
      <span class="wordmark__name"><span class="wordmark__mark"></span>Des Whitcombe Law</span>
      <span class="wordmark__rule"></span>
      <span class="wordmark__tag">Attorney at Law</span>
    </div>
    <dl class="contact">
      <div><dt>Tel:</dt> <dd>(510) 555-0183</dd></div>
      <div><dt>Fax:</dt> <dd>(510) 555-0162</dd></div>
      <div><dt>Email:</dt> <dd>deswhitcombelaw@mailbrook.net</dd></div>
      <div><dt>Web:</dt> <dd>www.deswhitcombelaw.net</dd></div>
    </dl>
  </section>

  <section class="piece card-front" aria-label="Business card front">
    <div class="wordmark wordmark--white">
      <span class="wordmark__name"><span class="wordmark__mark"></span>Des Whitcombe Law</span>
      <span class="wordmark__rule"></span>
      <span class="wordmark__tag">Attorney at Law</span>
    </div>
  </section>

  <section class="piece card-back" aria-label="Business card back">
    <div class="wordmark wordmark--navy">
      <span class="wordmark__name"><span class="wordmark__mark"></span>Des Whitcombe Law</span>
      <span class="wordmark__rule"></span>
      <span class="wordmark__tag">Attorney at Law</span>
    </div>
    <p class="card-back__name">Desmond R. Whitcombe, Attorney</p>
    <dl class="contact">
      <div><dt>Tel:</dt> <dd>(510) 555-0183</dd></div>
      <div><dt>Fax:</dt> <dd>(510) 555-0162</dd></div>
      <div><dt>Email:</dt> <dd>deswhitcombelaw@mailbrook.net</dd></div>
      <div><dt>Web:</dt> <dd>www.deswhitcombelaw.net</dd></div>
    </dl>
    <address class="card-back__address">735 Linden Avenue Suite 300<br>Oakland, California 94618</address>
    <div class="card-back__band"></div>
  </section>

</body>
</html>
```